Women's Online Clothing Boutique Needs Business Cards

I already have a logo that I would like to use. Some of the things that interest me is black business cards, foil embossed logo, glossy embossed logo, leopard print, no yellow font, rounded edges. I even like just a large logo on the front side with all of my information on the back side.

Contact Information for Business Card

https://copperfinch.shopvendly.example/
https://www.facebook.com/thecopperfinchboutique/
https://www.instagram.com/thecopperfinchboutique/
copperfinchboutique@mailora.example

Requirements
Must have
• My Logo
Nice to have
• Leopard Print
Should not have
• No Yellow Font

```html
<!DOCTYPE html>
<html lang="en">
<head>
<meta charset="utf-8">
<title>The Copper Finch Boutique – Business Cards</title>
<link rel="stylesheet" href="https://fonts.googleapis.com/css2?family=Montserrat:ital,wght@0,300;0,400;0,600;0,700;1,700&display=swap">
<style>
  :root {
    --page-bg: #dcdcdc;
    --card-black: #1c1c1e;
    --card-black-light: #2a2a2c;
    --silver: #cfcfcf;
    --print-light: #8a8a8c;
    --print-mid: #5e5e60;
    --print-dark: #303032;
    --band-white: #f4f4f4;
    --ink-dark: #1e1e1e;
  }
  * { box-sizing: border-box; margin: 0; padding: 0; }
  html, body { width: 1200px; height: 1200px; overflow: hidden; }
  body {
    background: var(--page-bg);
    font-family: "Montserrat", sans-serif;
    position: relative;
  }
  .card {
    position: absolute;
    left: 262px;
    width: 685px;
    height: 393px;
    border-radius: 20px;
    overflow: hidden;
    background: linear-gradient(160deg, var(--card-black-light) 0%, var(--card-black) 60%);
    box-shadow: 0 14px 24px rgba(0,0,0,0.25);
  }
  .card--front { top: 165px; }
  .card--back { top: 651px; }

  /* Front */
  .brand {
    position: absolute;
    left: 0; right: 0;
    top: 190px;
    text-align: center;
  }
  .brand__name {
    font-weight: 400;
    font-size: 36px;
    letter-spacing: 0;
    color: var(--silver);
  }
  .print-area {
    position: absolute;
    left: 0;
    width: 685px;
    display: block;
  }
  .card--front .print-area { bottom: 0; height: 72px; }
  .card--back .print-area { top: 0; height: 215px; }

  /* Back */
  .contact {
    position: absolute;
    left: 42px;
    top: 200px;
  }
  .contact__name {
    font-weight: 700;
    font-size: 19px;
    letter-spacing: 1px;
    color: #e6e6e6;
  }
  .contact__role {
    font-weight: 700;
    font-style: italic;
    font-size: 13px;
    color: #e6e6e6;
    margin-top: 2px;
  }
  .contact__list {
    list-style: none;
    margin-top: 28px;
    font-weight: 400;
    font-size: 14px;
    color: #d6d6d6;
  }
  .contact__list li {
    display: flex;
    align-items: center;
    gap: 12px;
    height: 21px;
  }
  .contact__list svg { width: 10px; height: 10px; fill: #cfcfcf; flex: none; }
  .web-band {
    position: absolute;
    left: 0; right: 0; bottom: 0;
    height: 52px;
    background: var(--band-white);
    display: flex;
    align-items: center;
    padding-left: 42px;
  }
  .web-band__url {
    font-weight: 700;
    font-style: italic;
    font-size: 13.5px;
    color: var(--ink-dark);
  }
</style>
</head>
<body>

  <section class="card card--front" aria-label="Business card front">
    <div class="brand">
      <span class="brand__name">The Copper Finch Boutique</span>
    </div>
    <svg class="print-area" viewBox="0 0 685 72" role="img" aria-label="Glossy embossed leopard print spots along the bottom edge">
      <defs>
        <linearGradient id="frontPrint" x1="0" y1="0" x2="1" y2="0">
          <stop offset="0" stop-color="var(--print-mid)"/>
          <stop offset="0.5" stop-color="var(--print-light)"/>
          <stop offset="1" stop-color="var(--print-dark)"/>
        </linearGradient>
      </defs>
      <path d="M0 18 C40 10 80 14 120 8 C170 2 210 12 260 10 C320 8 360 4 420 10 C480 14 530 6 590 10 C630 12 660 8 685 12 L685 72 L0 72 Z" fill="url(#frontPrint)" opacity="0.75"/>
    </svg>
  </section>

  <section class="card card--back" aria-label="Business card back">
    <svg class="print-area" viewBox="0 0 685 215" role="img" aria-label="Glossy embossed leopard print spots spreading from the top left down toward the right">
      <defs>
        <linearGradient id="backPrint" x1="0" y1="0" x2="1" y2="0.6">
          <stop offset="0" stop-color="var(--print-light)"/>
          <stop offset="0.45" stop-color="var(--print-mid)"/>
          <stop offset="1" stop-color="var(--print-dark)"/>
        </linearGradient>
      </defs>
      <path d="M0 0 L685 0 L685 160 C670 180 650 195 620 205 C590 210 560 190 530 180 C490 165 450 150 400 140 C340 130 280 128 220 125 C150 122 80 118 0 112 Z" fill="url(#backPrint)" opacity="0.8"/>
    </svg>

    <div class="contact">
      <p class="contact__name">DANIEL REYES</p>
      <p class="contact__role">President</p>
      <ul class="contact__list">
        <li>
          <svg viewBox="0 0 10 10" aria-hidden="true"><path d="M2 0.5 L3.6 2.6 L2.8 3.6 C3.4 5 4.8 6.5 6.3 7.2 L7.3 6.4 L9.5 8 L8.6 9.5 C4.5 9.2 0.8 5.5 0.5 1.4 Z"/></svg>
          <span>555-014-2271</span>
        </li>
        <li>
          <svg viewBox="0 0 10 10" aria-hidden="true"><path d="M0.5 2 H9.5 V8.5 H0.5 Z M0.5 2 L5 5.5 L9.5 2" fill="#cfcfcf" stroke="#1c1c1e" stroke-width="0.8"/></svg>
          <span>info@thecopperfinch.example</span>
        </li>
      </ul>
    </div>

    <div class="web-band">
      <span class="web-band__url">www.TheCopperFinchBoutique.example</span>
    </div>
  </section>

</body>
</html>
```